Business Card design for construction company

I would like a business card design for a construction company - Harlow Constructions. I have attached the ai logo file for use. I would like the card to be very smart and clean and incorporate only white and the two colours in the logo. I would like the card to have two sides. One side can just have the logo, the other with the relevant information.

Target Market(s)

Building and Construction Clients

Industry/Entity Type

Business

Contact Information for Business Card

Name: Tom Pardoe
Company: Harlow Constructions Pty Limited
Address: 14 Mallee Crescent Carrow Vale 2093
Phone: 0427 531 068
Email: tomp@harlowbuild-example.com.au

Font styles to use
Serif
Sans Serif

Requirements
Must have
• Details noted above
• Logo as provided
• Colours as in logo
• Square edges
• A font that compliments the logo
Should not have
• Any colour other than white and those in logo
• Rounded edges

```html
<!DOCTYPE html>
<html lang="en">
<head>
<meta charset="utf-8">
<title>Harlow Constructions – Business Card</title>
<link rel="stylesheet" href="https://fonts.googleapis.com/css2?family=Open+Sans:wght@400;600;700&family=Oswald:wght@500&display=swap">
<style>
  :root {
    --backdrop: #ececec;
    --charcoal: #58595b;
    --white: #ffffff;
    --accent-blue: #29a8e0;
    --ink: #4a4b4d;
  }
  * { margin: 0; padding: 0; box-sizing: border-box; }
  html, body {
    width: 1200px;
    height: 1000px;
    overflow: hidden;
    background: var(--backdrop);
  }
  .canvas {
    position: relative;
    width: 1200px;
    height: 1000px;
  }
  .card {
    position: absolute;
    left: 266px;
    width: 666px;
    height: 397px;
    box-shadow: 0 2px 6px rgba(0,0,0,0.18);
  }
  .card--front {
    top: 74px;
    background: var(--charcoal);
  }
  .card--back {
    top: 534px;
    background: var(--white);
  }
  .brand {
    position: absolute;
    left: 0;
    right: 0;
    top: 180px;
    display: flex;
    align-items: center;
    justify-content: center;
    gap: 16px;
  }
  .brand__mark {
    width: 12px;
    height: 12px;
    background: var(--accent-blue);
  }
  .brand__name {
    font-family: "Open Sans", sans-serif;
    font-weight: 600;
    font-size: 26px;
    letter-spacing: 3px;
    color: var(--white);
    text-transform: uppercase;
  }
  .contact {
    position: absolute;
    top: 176px;
    left: 0;
    width: 100%;
    height: 44px;
  }
  .contact__name {
    position: absolute;
    left: 95px;
    top: 2px;
    font-family: "Oswald", sans-serif;
    font-weight: 500;
    font-size: 31px;
    line-height: 40px;
    letter-spacing: -0.5px;
    color: var(--charcoal);
    text-transform: uppercase;
  }
  .contact__divider {
    position: absolute;
    left: 274px;
    top: 2px;
    width: 2px;
    height: 40px;
    background: var(--ink);
  }
  .contact__details {
    position: absolute;
    left: 307px;
    top: 1px;
    list-style: none;
    font-family: "Open Sans", sans-serif;
    font-size: 16px;
    line-height: 21px;
    color: var(--ink);
  }
  .contact__details li {
    display: flex;
    align-items: center;
    gap: 8px;
  }
  .contact__details svg { width: 15px; height: 12px; fill: var(--ink); }
  .company-line {
    position: absolute;
    left: 0;
    right: 0;
    top: 347px;
    text-align: center;
    font-family: "Open Sans", sans-serif;
    font-size: 16px;
    color: var(--ink);
  }
  .company-line strong { font-weight: 700; }
</style>
</head>
<body>
<main class="canvas">
  <section class="card card--front" aria-label="Card front">
    <div class="brand">
      <span class="brand__mark"></span>
      <span class="brand__name">Harlow Constructions</span>
    </div>
  </section>

  <section class="card card--back" aria-label="Card back">
    <div class="contact">
      <h1 class="contact__name">Tom Pardoe</h1>
      <span class="contact__divider"></span>
      <ul class="contact__details">
        <li>
          <svg viewBox="0 0 15 12" aria-hidden="true"><path d="M1 4 C1 1.5 14 1.5 14 4 L14 5 L10.5 5 L10.5 3.8 L4.5 3.8 L4.5 5 L1 5 Z M3.5 6 L11.5 6 L13 11 L2 11 Z"/></svg>
          0427 531 068
        </li>
        <li>
          <svg viewBox="0 0 15 12" aria-hidden="true"><path d="M1 2 H14 V11 H1 Z M2.2 3 L7.5 7 L12.8 3 Z" fill-rule="evenodd"/></svg>
          tomp@harlowbuild-example.com.au
        </li>
      </ul>
    </div>
    <p class="company-line"><strong>Harlow Constructions Pty Limited -</strong> 14 Mallee Crescent Carrow Vale 2093</p>
  </section>
</main>
</body>
</html>
```